Handover Document for post installation solar customers

I require a handover document (small A4 book) design for when we complete solar installations for our customers. It will need to have a brief description of next steps off the application process after installation aswell as some maintenance scheduling etc. This information will be provided by us.

Target Market(s)

Post installation customers (Solar)

Industry/Entity Type

Solar/ renewable

Colors
0054AA
0677BA
7BADD7
CADEEF
E8F1F8

Requirements
Must have
• Handover document provided in attatchment (must be made generic and not include customers details etc.) the attachment is only for reference. An intro "Thanks for using VORA electrics.........". What happens next section
Nice to have
• Please use some of our past customers logos in our website - www.voraelectrics.com.au
Should not have
• Must be simple and look professional

```html
<!DOCTYPE html>
<html lang="en">
<head>
<meta charset="utf-8">
<title>VORA electrics – Solar System Owner's Manual</title>
<link href="https://fonts.googleapis.com/css2?family=Montserrat:wght@400;500;600;700;800&display=swap" rel="stylesheet">
<style>
:root{
  --board:#74acd8;
  --blue-dark:#0054AA;
  --blue:#0677BA;
  --blue-mid:#7BADD7;
  --blue-light:#CADEEF;
  --blue-pale:#E8F1F8;
  --ink:#111;
  --grey:#3a3a3a;
  --text:#555;
  --warn:#d62b2b;
  --white:#fff;
}
*{margin:0;padding:0;box-sizing:border-box}
html,body{width:1200px;height:1095px;overflow:hidden;background:var(--board);font-family:"Montserrat",sans-serif;color:var(--text)}
.board{position:relative;width:1200px;height:1095px}

/* cover */
.cover{position:absolute;left:469px;top:25px;width:240px;height:338px;background:var(--white);overflow:hidden;box-shadow:0 6px 10px rgba(0,0,0,.25)}
.cover svg.art{position:absolute;left:0;top:0}
.brand{position:absolute;display:flex;align-items:center;gap:3px;font-weight:800;color:var(--blue-dark)}
.brand .mark{border:2px solid var(--blue);border-radius:2px}
.brand .name{line-height:1}
.brand .name small{display:block;font-weight:700;color:var(--blue);letter-spacing:1px}
.cover .brand{right:14px;top:20px}
.cover .brand .mark{width:22px;height:22px}
.cover .brand .name{font-size:22px}
.cover .brand .name small{font-size:6px;text-align:right}
.title-pill{position:absolute;background:var(--blue);color:var(--white);font-weight:500;border-radius:0 10px 10px 0}
.title-main{position:absolute;font-weight:800;color:var(--ink)}
.cover .title-pill{left:14px;top:294px;font-size:9px;padding:1px 14px 1px 4px}
.cover .title-main{left:18px;top:306px;font-size:16px}

/* spreads */
.spread{position:absolute;width:280px;height:197px;background:var(--white);box-shadow:0 5px 8px rgba(0,0,0,.22);overflow:hidden}
.spread .deco{position:absolute;left:0;top:0}
.spread .fold{position:absolute;left:140px;top:0;width:1px;height:100%;background:#eee}
.page{position:absolute;top:0;width:140px;height:197px;padding:27px 8px 0}
.page.l{left:0}.page.r{left:140px}
.mini-brand{position:absolute;top:8px;display:flex;align-items:center;gap:1px;font-weight:800;color:var(--grey);font-size:7px;line-height:1}
.mini-brand .mark{width:6px;height:6px;border:1px solid var(--blue)}
.mini-brand small{display:block;font-size:1.6px;color:var(--blue);letter-spacing:.3px}
.page.l .mini-brand{right:6px}
.page.r .mini-brand{left:6px}
.url{position:absolute;bottom:3px;font-size:2.4px;color:var(--ink)}
.page.l .url{left:8px}.page.r .url{right:8px}
.pno{position:absolute;bottom:12px;font-size:2.2px;color:var(--ink)}
.page.l .pno{left:8px}.page.r .pno{right:8px}
.tag{display:inline-block;background:var(--blue);color:var(--white);font-size:2.6px;font-weight:700;padding:.6px 3px;border-radius:2px;margin:2px 0 3px}
.h{font-size:2.6px;font-weight:700;color:var(--ink);margin:2px 0 1px}
.hb{font-size:2.6px;font-weight:700;color:var(--blue);margin:2px 0 1px}
.p{font-size:2px;line-height:1.35;margin-bottom:2px}
.row{border:.4px solid #ccc;border-radius:2px;height:4px;margin-bottom:1.4px;font-size:1.8px;padding:.8px 2px;color:var(--ink);display:flex;justify-content:space-between}
.thead{background:var(--grey);color:var(--white);border-radius:1px;font-size:2px;font-weight:700;padding:.6px 3px;display:flex;justify-content:space-between;margin-bottom:1.4px}
.thead.blue{background:var(--blue)}
.warn{border:.6px solid var(--warn);border-radius:5px;padding:2px 4px;margin:3px 0;text-align:center;font-size:1.8px}
.warn b{display:block;color:var(--warn);font-size:2.2px}
.toc{font-size:2.3px;color:var(--ink);margin:3px 0 0}
.toc b{font-weight:700}
.toc span{display:block;color:var(--blue);padding-left:8px;font-size:2.1px}
.figure{border-radius:2px}

/* back cover */
.backcover{position:absolute;left:0;top:0;width:140px;height:197px;background:linear-gradient(160deg,#2a2e36,#0d0f14)}
.clients{position:absolute;left:17px;top:66px;width:106px;height:65px;background:var(--white);border-radius:6px;display:grid;grid-template-columns:repeat(4,1fr);gap:4px;padding:7px}
.clients i{display:block;background:var(--blue-light);border-radius:2px}
.backcover .brand{left:40px;top:146px;color:var(--white)}
.backcover .brand .mark{width:13px;height:13px;border-color:var(--white)}
.backcover .brand .name{font-size:13px}
.backcover .brand .name small{font-size:3.2px;color:var(--white)}
.backcover .addr{position:absolute;left:0;width:140px;top:180px;text-align:center;color:var(--white);font-size:2.3px;line-height:1.4}
.frontmini{position:absolute;left:140px;top:0;width:140px;height:197px;overflow:hidden;background:var(--white)}
.frontmini .brand{right:8px;top:10px}
.frontmini .brand .mark{width:12px;height:12px}
.frontmini .brand .name{font-size:12px}
.frontmini .brand .name small{font-size:3.2px;text-align:right}
.frontmini .title-pill{left:10px;top:170px;font-size:5px;padding:.5px 8px .5px 3px}
.frontmini .title-main{left:11px;top:177px;font-size:9px}
</style>
</head>
<body>
<main class="board">

  <!-- front cover -->
  <section class="cover">
    <svg class="art" width="240" height="338" viewBox="0 0 240 338">
      <path d="M0 10 C60 30 120 80 240 60 L240 240 C170 270 60 240 0 250 Z" fill="#cfd7df"/>
      <path d="M0 250 C70 240 150 270 240 236 L240 250 C150 290 60 262 0 275 Z" fill="var(--blue)"/>
      <path d="M0 275 C60 262 160 285 240 250 L240 262 C150 300 70 278 0 292 Z" fill="#2b2b2b"/>
      <path d="M120 120 C160 90 200 95 240 92 L240 122 C200 118 170 125 130 140 Z" fill="#2b2b2b"/>
      <path d="M0 0 L60 0 C30 40 10 90 0 140 Z" fill="#e7e9ec"/>
    </svg>
    <div role="img" aria-label="Photo of a solar technician in hard hat and safety vest holding a tablet among solar panels" style="position:absolute;left:0;top:60px;width:180px;height:190px;background:linear-gradient(140deg,#c7b08a,#e7742a 55%,#6f7b86);clip-path:ellipse(85% 55% at 30% 55%);opacity:.9"></div>
    <div class="brand"><span class="mark"></span><span class="name">VORA<small>ELECTRICS</small></span></div>
    <div class="title-pill">SOLAR SYSTEM</div>
    <div class="title-main">OWNER'S MANUAL</div>
  </section>

  <!-- spread: back + front -->
  <section class="spread" style="left:15px;top:423px">
    <div class="backcover">
      <div class="clients" aria-label="Past customer badges">
        <i></i><i></i><i></i><i></i><i></i><i></i><i></i><i></i><i></i><i></i><i></i><i></i><i></i><i></i><i></i><i></i>
      </div>
      <div class="brand"><span class="mark"></span><span class="name">VORA<small>ELECTRICS</small></span></div>
      <div class="addr">12/80 HARBOUR ROAD, EASTVALE, VIC 3000<br>INFO@VORAELECTRICS.COM.AU | (03) 9000 0000</div>
    </div>
    <div class="frontmini">
      <svg width="140" height="197" viewBox="0 0 140 197" style="position:absolute;left:0;top:0">
        <path d="M0 8 C40 20 90 40 140 30 L140 140 C100 160 40 140 0 146 Z" fill="#cfd7df"/>
        <path d="M0 146 C40 140 90 158 140 138 L140 146 C90 168 40 152 0 160 Z" fill="var(--blue)"/>
        <path d="M0 160 C40 152 90 166 140 146 L140 153 C90 175 40 162 0 170 Z" fill="#2b2b2b"/>
      </svg>
      <div role="img" aria-label="Photo of a solar technician among solar panels" style="position:absolute;left:0;top:35px;width:110px;height:110px;background:linear-gradient(140deg,#c7b08a,#e7742a 55%,#6f7b86);clip-path:ellipse(85% 55% at 30% 55%)"></div>
      <div class="brand"><span class="mark"></span><span class="name">VORA<small>ELECTRICS</small></span></div>
      <div class="title-pill">SOLAR SYSTEM</div>
      <div class="title-main">OWNER'S MANUAL</div>
    </div>
  </section>

  <!-- spread template deco used in each -->
  <!-- spread 01-02 -->
  <section class="spread" style="left:312px;top:423px">
    <svg class="deco" width="280" height="197" viewBox="0 0 280 197">
      <path d="M0 0 H30 C20 4 12 10 8 16 C10 8 4 4 0 3Z" fill="#222"/>
      <path d="M0 0 H35 C22 2 12 6 6 14 C6 6 3 3 0 2Z" fill="var(--blue)" transform="translate(0,2)"/>
      <path d="M280 0 H250 C260 4 268 10 272 16 C270 8 276 4 280 3Z" fill="#222"/>
      <path d="M280 2 H245 C258 4 268 8 274 16 C274 8 277 5 280 4Z" fill="var(--blue)"/>
      <rect x="0" y="187" width="280" height="1.5" fill="#111"/>
      <path d="M105 197 C120 180 160 180 175 197Z" fill="#111"/>
      <path d="M112 197 C125 185 155 185 168 197Z" fill="var(--blue)"/>
    </svg>
    <div class="fold"></div>
    <div class="page l">
      <div class="mini-brand"><span class="mark"></span><span>VORA<small>ELECTRICS</small></span></div>
      <div class="tag">Contents</div>
      <div class="toc"><b>01 - Introduction</b></div>
      <div class="toc"><b>02 - Contact Information</b><span>2.1 Installation Company</span><span>2.2 Accredited Installer</span></div>
      <div class="toc"><b>03 - Precautions and warnings</b><span>3.1 Warning symbols</span><span>3.2 Important Safety Information</span></div>
      <div class="toc"><b>04 - Emergency Procedures</b><span>4.1 Earth Fault Alarm</span><span>4.2 Shutdown Procedure</span></div>
      <div class="toc"><b>05 - System Description</b><span>5.1 PV System Summary</span><span>5.2 Components</span><span>5.3 System Configuration</span></div>
      <div class="toc"><b>09 - Maintenance Information</b><span>9.1 Recommended Maintenance Schedule</span><span>9.2 Information for Maintenance Staff</span><span>9.3 Maintenance Logs</span></div>
      <div class="toc"><b>10 - Commissioning Report</b><span>10.1 Installation Checklist</span><span>10.2 Test Records</span><span>10.3 Declaration of Compliance</span></div>
      <div class="toc"><b>11 - Warranty Information</b></div>
      <div class="pno">01</div><div class="url">www.voraelectric.com</div>
    </div>
    <div class="page r">
      <div class="mini-brand"><span class="mark"></span><span>VORA<small>ELECTRICS</small></span></div>
      <div class="tag">Introduction</div>
      <p class="p">Thanks for choosing VORA electrics for your new solar system. Your system will help cut power bills and reduce emissions for years to come.</p>
      <p class="p">Please read this manual carefully. It explains how your system works, how to operate it safely and how to keep it well maintained.</p>
      <p class="p">Keep this manual in a safe place for future reference.</p>
      <div class="pno">02</div><div class="url">www.voraelectric.com</div>
    </div>
  </section>

  <!-- spread 03-04 -->
  <section class="spread" style="left:608px;top:423px">
    <svg class="deco" width="280" height="197" viewBox="0 0 280 197">
      <path d="M0 0 H30 C20 4 12 10 8 16 C10 8 4 4 0 3Z" fill="#222"/>
      <path d="M0 2 H35 C22 4 12 8 6 16 C6 8 3 5 0 4Z" fill="var(--blue)"/>
      <path d="M280 0 H250 C260 4 268 10 272 16 C270 8 276 4 280 3Z" fill="#222"/>
      <path d="M280 2 H245 C258 4 268 8 274 16 C274 8 277 5 280 4Z" fill="var(--blue)"/>
      <rect x="0" y="187" width="280" height="1.5" fill="#111"/>
      <path d="M105 197 C120 180 160 180 175 197Z" fill="#111"/>
      <path d="M112 197 C125 185 155 185 168 197Z" fill="var(--blue)"/>
    </svg>
    <div class="fold"></div>
    <div class="page l">
      <div class="mini-brand"><span class="mark"></span><span>VORA<small>ELECTRICS</small></span></div>
      <div class="tag">Post Installation Procedure</div>
      <p class="p">After installation we will book an electrical inspector to visit your site. This can take up to ten working days. Your system will be left switched off until the inspector deems it safe.</p>
      <div class="h">System has been turned on</div>
      <p class="p">Once inspection is complete your system is turned on and we notify your retailer to arrange your new meter.</p>
      <div class="pno">03</div><div class="url">www.voraelectric.com</div>
    </div>
    <div class="page r">
      <div class="mini-brand"><span class="mark"></span><span>VORA<small>ELECTRICS</small></span></div>
      <div class="tag">Contact Information</div>
      <div class="h">2.1 Installation Company</div>
      <div class="row">Company Name</div>
      <div class="h">2.2 Accredited Installer</div>
      <div class="row">Name</div>
      <div class="tag">Precautions and Warnings</div>
      <p class="p">Your system runs automatically with no need for user input. High DC and AC voltages are present, so please read all warnings.</p>
      <div class="h">3.1 Warning Symbols</div>
      <svg width="124" height="14" viewBox="0 0 124 14"><path d="M7 1 L13 13 H1Z" fill="#f5c400" stroke="#111" stroke-width=".6"/><text x="16" y="6" font-size="2" fill="#555">General safety warning</text><path d="M69 1 L75 13 H63Z" fill="#f5c400" stroke="#111" stroke-width=".6"/><text x="78" y="6" font-size="2" fill="#555">Electrical safety warning</text></svg>
      <div class="h">3.2 Important Safety Information</div>
      <p class="p">• Do not attempt service unless you are a licensed electrician.<br>• Do not open components of the system.<br>• Do not climb onto the roof to clean panels.</p>
      <div class="pno">04</div><div class="url">www.voraelectric.com</div>
    </div>
  </section>

  <!-- spread 05-06 -->
  <section class="spread" style="left:900px;top:423px">
    <svg class="deco" width="280" height="197" viewBox="0 0 280 197">
      <path d="M0 0 H30 C20 4 12 10 8 16 C10 8 4 4 0 3Z" fill="#222"/>
      <path d="M0 2 H35 C22 4 12 8 6 16 C6 8 3 5 0 4Z" fill="var(--blue)"/>
      <path d="M280 0 H250 C260 4 268 10 272 16 C270 8 276 4 280 3Z" fill="#222"/>
      <path d="M280 2 H245 C258 4 268 8 274 16 C274 8 277 5 280 4Z" fill="var(--blue)"/>
      <rect x="0" y="187" width="280" height="1.5" fill="#111"/>
      <path d="M105 197 C120 180 160 180 175 197Z" fill="#111"/>
      <path d="M112 197 C125 185 155 185 168 197Z" fill="var(--blue)"/>
    </svg>
    <div class="fold"></div>
    <div class="page l">
      <div class="mini-brand"><span class="mark"></span><span>VORA<small>ELECTRICS</small></span></div>
      <p class="p">• Observe all safety signage on the system.<br>• Know the shutdown procedure and the Earth Fault Alarm.<br>• Isolate the system fully before any work.</p>
      <div class="tag">Emergency Procedures</div>
      <p class="p">If a fault occurs or the system must be shut down, follow the steps below.</p>
      <div class="warn"><b>WARNING:</b>Follow steps in order. Arcing may occur if not.</div>
      <div class="h">4.1 Earth Fault Alarm</div>
      <p class="p">If a fault to earth occurs the inverter will signal an alarm by LED, display message or email alert.</p>
      <p class="p">1. Follow the shutdown procedure.<br>2. Limit access to the system.<br>3. Call VORA electrics for service.</p>
      <div class="pno">05</div><div class="url">www.voraelectric.com</div>
    </div>
    <div class="page r">
      <div class="mini-brand"><span class="mark"></span><span>VORA<small>ELECTRICS</small></span></div>
      <div class="h">4.2 Shutdown Procedure</div>
      <div class="figure" role="img" aria-label="Shutdown procedure diagram showing inverter, isolators and switchboard" style="height:50px;background:linear-gradient(135deg,var(--blue-pale),var(--blue-light))"></div>
      <div class="hb" style="text-align:center">Shutdown procedure diagram</div>
      <div class="thead"><span>Number</span><span>Description</span></div>
      <div class="row" style="background:var(--blue-light);border:0">1 <span>PV DC isolator</span></div>
      <div class="row" style="background:var(--blue-light);border:0">2 <span>Inverter</span></div>
      <div class="row" style="background:var(--blue-light);border:0">3 <span>Inverter AC isolator</span></div>
      <div class="row" style="background:var(--blue-light);border:0">4 <span>Main switch</span></div>
      <p class="p">1. Turn main switch off. 2. Turn AC isolator off. 3. Turn DC isolator off.</p>
      <div class="warn"><b>WARNING:</b>Current may still be present after shutdown.</div>
      <div class="warn"><b>WARNING:</b>Do not turn on if the system is water damaged.</div>
      <div class="pno">06</div><div class="url">www.voraelectric.com</div>
    </div>
  </section>

  <!-- spread 07-08 -->
  <section class="spread" style="left:15px;top:640px">
    <svg class="deco" width="280" height="197" viewBox="0 0 280 197">
      <path d="M0 0 H30 C20 4 12 10 8 16 C10 8 4 4 0 3Z" fill="#222"/>
      <path d="M0 2 H35 C22 4 12 8 6 16 C6 8 3 5 0 4Z" fill="var(--blue)"/>
      <path d="M280 0 H250 C260 4 268 10 272 16 C270 8 276 4 280 3Z" fill="#222"/>
      <path d="M280 2 H245 C258 4 268 8 274 16 C274 8 277 5 280 4Z" fill="var(--blue)"/>
      <rect x="0" y="187" width="280" height="1.5" fill="#111"/>
      <path d="M105 197 C120 180 160 180 175 197Z" fill="#111"/>
      <path d="M112 197 C125 185 155 185 168 197Z" fill="var(--blue)"/>
    </svg>
    <div class="fold"></div>
    <div class="page l">
      <div class="mini-brand"><span class="mark"></span><span>VORA<small>ELECTRICS</small></span></div>
      <div class="tag">System Description</div>
      <p class="p">Your grid-connected solar system converts sunlight into electricity for use in your home, with any surplus exported to the grid.</p>
      <div class="figure" role="img" aria-label="Diagram of solar system on a house connected to the grid" style="height:52px;background:linear-gradient(135deg,var(--blue-pale),var(--blue-light))"></div>
      <div class="thead"><span>Number</span><span>Description</span></div>
      <div class="row" style="background:var(--blue-light);border:0">1<span>Solar Panel Array</span></div>
      <div class="row" style="background:var(--blue-light);border:0">2<span>Inverter</span></div>
      <div class="row" style="background:var(--blue-light);border:0">3<span>Meter</span></div>
      <div class="h">5.1 PV System Summary</div>
      <div class="row">Type</div><div class="row">Maximum System Output</div><div class="row">Estimated Annual Production</div><div class="row">Inverter Rating</div>
      <div class="pno">07</div><div class="url">www.voraelectric.com</div>
    </div>
    <div class="page r">
      <div class="mini-brand"><span class="mark"></span><span>VORA<small>ELECTRICS</small></span></div>
      <div class="h">5.2 Components</div>
      <div class="hb">Solar PV Modules</div>
      <p class="p">Solar panels convert sunlight into DC electricity and are mounted on your roof for best exposure.</p>
      <div class="row">Brand</div><div class="row">Model</div><div class="row">Power rating</div><div class="row">Efficiency</div>
      <div class="hb">Inverter</div>
      <p class="p">The inverter converts DC power from the panels into AC power for your home.</p>
      <div class="row">Brand</div><div class="row">Model</div><div class="row">AC output power rating</div><div class="row">Efficiency</div><div class="row">Brand</div><div class="row">Model</div>
      <div class="pno">08</div><div class="url">www.voraelectric.com</div>
    </div>
  </section>

  <!-- spread 09-10 -->
  <section class="spread" style="left:312px;top:640px">
    <svg class="deco" width="280" height="197" viewBox="0 0 280 197">
      <path d="M0 0 H30 C20 4 12 10 8 16 C10 8 4 4 0 3Z" fill="#222"/>
      <path d="M0 2 H35 C22 4 12 8 6 16 C6 8 3 5 0 4Z" fill="var(--blue)"/>
      <path d="M280 0 H250 C260 4 268 10 272 16 C270 8 276 4 280 3Z" fill="#222"/>
      <path d="M280 2 H245 C258 4 268 8 274 16 C274 8 277 5 280 4Z" fill="var(--blue)"/>
      <rect x="0" y="187" width="280" height="1.5" fill="#111"/>
      <path d="M105 197 C120 180 160 180 175 197Z" fill="#111"/>
      <path d="M112 197 C125 185 155 185 168 197Z" fill="var(--blue)"/>
    </svg>
    <div class="fold"></div>
    <div class="page l">
      <div class="mini-brand"><span class="mark"></span><span>VORA<small>ELECTRICS</small></span></div>
      <p class="p">Full inverter specifications are listed in the supplied user manual.</p>
      <div class="hb">Isolators</div>
      <p class="p">Isolators are manual switches used to disconnect parts of the circuit safely.</p>
      <div class="h">AC Isolators</div>
      <p class="p">The AC isolator disconnects the inverter from the switchboard.</p>
      <div class="h">DC Isolators</div>
      <p class="p">The DC isolator disconnects the solar array from the inverter.</p>
      <div class="hb">Cabling</div>
      <p class="p">Cables are rated for outdoor use and kept in conduit where required.</p>
      <div class="hb">Electricity Meter</div>
      <p class="p">The meter records energy used and exported. Your retailer will arrange any meter upgrade.</p>
      <div class="pno">09</div><div class="url">www.voraelectric.com</div>
    </div>
    <div class="page r">
      <div class="mini-brand"><span class="mark"></span><span>VORA<small>ELECTRICS</small></span></div>
      <div class="h">5.3 System Configuration</div>
      <div class="thead">MPPT 1</div>
      <div class="row">Sub-Array Power</div><div class="row">String A panel count</div><div class="row">String B panel count</div>
      <div class="thead">MPPT 2</div>
      <div class="row">Sub-Array Power</div><div class="row">String C panel count</div><div class="row">String D panel count</div>
      <div class="h">9.1 Recommended Maintenance Schedule</div>
      <p class="p">We recommend a professional service once a year.</p>
      <div class="thead blue"><span>Maintenance action</span><span>Frequency</span><span>Action</span></div>
      <div class="row"><span>Check for debris</span><span>Quarterly</span></div>
      <div class="row"><span>Check trees for shading</span><span>Quarterly</span></div>
      <div class="pno">10</div><div class="url">www.voraelectric.com</div>
    </div>
  </section>

  <!-- spread 11-12 -->
  <section class="spread" style="left:608px;top:640px">
    <svg class="deco" width="280" height="197" viewBox="0 0 280 197">
      <path d="M0 0 H30 C20 4 12 10 8 16 C10 8 4 4 0 3Z" fill="#222"/>
      <path d="M0 2 H35 C22 4 12 8 6 16 C6 8 3 5 0 4Z" fill="var(--blue)"/>
      <path d="M280 0 H250 C260 4 268 10 272 16 C270 8 276 4 280 3Z" fill="#222"/>
      <path d="M280 2 H245 C258 4 268 8 274 16 C274 8 277 5 280 4Z" fill="var(--blue)"/>
      <rect x="0" y="187" width="280" height="1.5" fill="#111"/>
      <path d="M105 197 C120 180 160 180 175 197Z" fill="#111"/>
      <path d="M112 197 C125 185 155 185 168 197Z" fill="var(--blue)"/>
    </svg>
    <div class="fold"></div>
    <div class="page l">
      <div class="mini-brand"><span class="mark"></span><span>VORA<small>ELECTRICS</small></span></div>
      <div style="background:var(--blue);color:#fff;border-radius:4px;padding:3px;font-size:2.2px;font-weight:700;display:flex;justify-content:space-between;margin-bottom:3px"><span>Visually check PV modules</span><span>Annually</span><span>Inspect and replace</span></div>
      <div class="row">a. Fractures</div><div class="row">b. Browning</div><div class="row">c. Moisture</div>
      <div class="hb">Inverter</div>
      <div class="row"><span>Check inverter is operating</span><span>Weekly</span></div>
      <div class="row"><span>Check internet connection</span><span>Quarterly</span></div>
      <div class="row"><span>Check ventilation filters</span><span>Annually</span></div>
      <div class="hb">Wiring Installation</div>
      <div class="row"><span>Check conduits</span><span>5 year</span></div>
      <div class="row"><span>Test operation of switches</span><span>Annually</span></div>
      <div class="row"><span>Check connections</span><span>Annually</span></div>
      <div class="pno">11</div><div class="url">www.voraelectric.com</div>
    </div>
    <div class="page r">
      <div class="mini-brand"><span class="mark"></span><span>VORA<small>ELECTRICS</small></span></div>
      <div class="row"><span>Check junction boxes</span><span>Annually</span></div>
      <div class="row"><span>Check seals</span><span>Annually</span></div>
      <div class="row"><span>Check cable entries</span><span>Annually</span></div>
      <div class="row"><span>Verify blocking diodes</span><span>Annually</span></div>
      <div class="thead blue"><span>Maintenance action</span><span>Frequency</span><span>Action</span></div>
      <div class="row"><span>Check surge arresters</span><span>Annually</span></div>
      <div class="h">Electrical Characteristics</div>
      <div class="row"><span>Record open circuit voltages</span><span>Annually</span></div>
      <div class="row"><span>Record short circuit currents</span><span>Annually</span></div>
      <div class="h">Protective Devices</div>
      <div class="row"><span>Verify fuse holders</span><span>Annually</span></div>
      <div class="row"><span>Verify circuit breakers</span><span>Annually</span></div>
      <div class="pno">12</div><div class="url">www.voraelectric.com</div>
    </div>
  </section>

  <!-- spread 13-14 -->
  <section class="spread" style="left:900px;top:640px">
    <svg class="deco" width="280" height="197" viewBox="0 0 280 197">
      <path d="M0 0 H30 C20 4 12 10 8 16 C10 8 4 4 0 3Z" fill="#222"/>
      <path d="M0 2 H35 C22 4 12 8 6 16 C6 8 3 5 0 4Z" fill="var(--blue)"/>
      <path d="M280 0 H250 C260 4 268 10 272 16 C270 8 276 4 280 3Z" fill="#222"/>
      <path d="M280 2 H245 C258 4 268 8 274 16 C274 8 277 5 280 4Z" fill="var(--blue)"/>
      <rect x="0" y="187" width="280" height="1.5" fill="#111"/>
      <path d="M105 197 C120 180 160 180 175 197Z" fill="#111"/>
      <path d="M112 197 C125 185 155 185 168 197Z" fill="var(--blue)"/>
    </svg>
    <div class="fold"></div>
    <div class="page l">
      <div class="mini-brand"><span class="mark"></span><span>VORA<small>ELECTRICS</small></span></div>
      <div class="row">Mounting system</div>
      <div class="row"><span>Check bolts and clamps</span><span>Annually</span></div>
      <div class="row"><span>Check for corrosion</span><span>Annually</span></div>
      <div class="row"><span>Check for corrosion</span><span>Annually</span></div>
      <div class="row">Other</div>
      <div class="row"><span>Check labelling is visible</span><span>Annually</span></div>
      <div style="height:20px"></div>
      <div class="warn"><b>WARNING:</b>Do not touch a broken or cracked module.</div>
      <div class="warn"><b>WARNING:</b>Use trained professionals for work at heights.</div>
      <div class="pno">13</div><div class="url">www.voraelectric.com</div>
    </div>
    <div class="page r">
      <div class="mini-brand"><span class="mark"></span><span>VORA<small>ELECTRICS</small></span></div>
      <div class="tag">Appendix C - Disclaimers</div>
      <div class="h">C1 – User Manual</div>
      <p class="p">This manual follows current Australian standards and clean energy guidelines. Read it alongside the component manuals.</p>
      <div class="h">C2 – Performance Estimate</div>
      <p class="p">Energy output is an estimate based on site data and past weather. Actual results will vary with shading, weather and usage, and savings are not guaranteed.</p>
      <div class="h">C3 – Copyright</div>
      <p class="p">This publication is copyright. No part may be reproduced without written consent from VORA electrics.</p>
      <div class="pno">14</div><div class="url">www.voraelectric.com</div>
    </div>
  </section>

  <!-- spread 15-16 -->
  <section class="spread" style="left:460px;top:875px;width:280px;height:214px">
    <svg class="deco" width="280" height="214" viewBox="0 0 280 214">
      <path d="M0 0 H30 C20 4 12 10 8 16 C10 8 4 4 0 3Z" fill="#222"/>
      <path d="M0 2 H35 C22 4 12 8 6 16 C6 8 3 5 0 4Z" fill="var(--blue)"/>
      <path d="M280 0 H250 C260 4 268 10 272 16 C270 8 276 4 280 3Z" fill="#222"/>
      <path d="M280 2 H245 C258 4 268 8 274 16 C274 8 277 5 280 4Z" fill="var(--blue)"/>
      <rect x="0" y="204" width="280" height="1.5" fill="#111"/>
      <path d="M105 214 C120 197 160 197 175 214Z" fill="#111"/>
      <path d="M112 214 C125 202 155 202 168 214Z" fill="var(--blue)"/>
    </svg>
    <div class="fold"></div>
    <div class="page l" style="height:214px">
      <div class="mini-brand"><span class="mark"></span><span>VORA<small>ELECTRICS</small></span></div>
      <div class="tag">Appendix D - Commissioning</div>
      <div class="pno">15</div><div class="url">www.voraelectric.com</div>
    </div>
    <div class="page r" style="height:214px">
      <div class="mini-brand"><span class="mark"></span><span>VORA<small>ELECTRICS</small></span></div>
      <div class="tag">Appendix E - Attachments</div>
      <div class="pno">16</div><div class="url">www.voraelectric.com</div>
    </div>
  </section>

</main>
</body>
</html>
```